VELVET ORBITS - BOOK COVER

I have written a book called VELVET ORBIT - HOW TO CLIMB PAST EVERY LIMIT TO THE TOP RUNG. I need a front cover design for the book. The book cover needs to be intriguing for someone to pick it up and read the first couple of pages. I want people to think about ACHIEVING SUCCESS when they read this book.
PLEASE LOOK AT THE ATTACHMENT. THANKS!

Target Market(s)

males, entrepreneurs, small business owners, salespeople, corporate executives

Industry/Entity Type

Business

Logo Text

VELVET ORBITS

Logo styles of interest
Emblem Logo
Abstract Logo
Font styles to use
Serif
Sans Serif

Colors
ec1f27
000000
959595
ffffff

Requirements
Must have
• It has to have a "hurricane" feel to it with hurricane colors.
Nice to have
• I open to your ideas
Should not have
• no other colors except red, black, gray, white.

```html
<!DOCTYPE html>
<html lang="en">
<head>
<meta charset="utf-8">
<title>Velvet Orbits – Book Cover</title>
<link href="https://fonts.googleapis.com/css2?family=Bebas+Neue&family=Oswald:wght@500;600&display=swap" rel="stylesheet">
<style>
  :root {
    --red: #ec1f27;
    --black: #000000;
    --ink: #1a1a1a;
    --gray: #959595;
    --white: #ffffff;
    --paper: #eef1f3;
  }
  * { margin: 0; padding: 0; box-sizing: border-box; }
  html, body {
    width: 1200px;
    height: 1000px;
    overflow: hidden;
    background: var(--white);
  }
  .stage {
    position: relative;
    width: 1200px;
    height: 1000px;
    display: flex;
    align-items: center;
    justify-content: center;
  }
  .cover {
    position: relative;
    width: 560px;
    height: 820px;
    background: var(--paper);
    overflow: hidden;
  }
  .storm-art {
    position: absolute;
    left: 0;
    top: 0;
    width: 100%;
    height: 560px;
    background:
      radial-gradient(ellipse 70% 55% at 40% 78%, var(--paper) 0%, rgba(238,241,243,0.9) 40%, rgba(238,241,243,0) 72%),
      linear-gradient(180deg, #2a2a2a 0%, #3c3c3c 35%, var(--gray) 70%, var(--paper) 100%);
  }
  .storm-art::after {
    content: "";
    position: absolute;
    right: 0;
    top: 0;
    width: 40%;
    height: 100%;
    background: linear-gradient(90deg, rgba(42,42,42,0) 0%, rgba(42,42,42,0.85) 100%);
  }
  .title-block {
    position: absolute;
    left: 96px;
    top: 470px;
  }
  .book-title {
    font-family: "Bebas Neue", "Oswald", sans-serif;
    font-weight: 400;
    color: var(--red);
    font-size: 128px;
    line-height: 0.84;
    letter-spacing: 1px;
  }
  .book-subtitle {
    margin-top: 12px;
    font-family: "Oswald", sans-serif;
    font-weight: 600;
    font-size: 14px;
    letter-spacing: 0.4px;
    color: var(--ink);
    text-transform: uppercase;
  }
  .book-author {
    margin-top: 16px;
    font-family: "Oswald", sans-serif;
    font-weight: 500;
    font-size: 34px;
    color: var(--black);
    text-transform: uppercase;
  }
</style>
</head>
<body>
  <main class="stage">
    <section class="cover">
      <div class="storm-art" role="img" aria-label="Abstract swirl of shattered black and gray shards forming a hurricane arc"></div>
      <div class="title-block">
        <h1 class="book-title">Velvet<br>Orbits</h1>
        <p class="book-subtitle">How to climb past every limit to the top rung</p>
        <p class="book-author">By Dale Renwick</p>
      </div>
    </section>
  </main>
</body>
</html>
```